Law Offices business card

Hi there, I'll need business card for the Law Offices of Tobin Haskell. The information must convey his strategic approach and quick resolution to complex business litigation needs. Please emphasize Civil Litigation, Corporate Law, Business Governance and Real Estate Law. Tobin has over 25 years of experience in these fields.The card should be modern and edgy and the message should be clear. Please consult his current website for ideas.

Business

```html
<!DOCTYPE html>
<html lang="en">
<head>
<meta charset="utf-8">
<title>Law Offices of Tobin Haskell — Business Card</title>
<link rel="stylesheet" href="https://fonts.googleapis.com/css2?family=EB+Garamond:wght@400&family=Arimo:ital,wght@0,400;1,400&display=swap">
<style>
  :root {
    --paper: #ffffff;
    --crop-mark: #1a1a1a;
    --gold-light: #bb944c;
    --gold-mid: #9a7034;
    --bronze-dark: #6f461d;
    --ink-light: #ffffff;
  }
  * { margin: 0; padding: 0; box-sizing: border-box; }
  html, body {
    width: 1200px;
    height: 759px;
    overflow: hidden;
    background: var(--paper);
  }
  .sheet {
    position: relative;
    width: 1200px;
    height: 759px;
  }
  .crop-marks {
    position: absolute;
    inset: 0;
  }
  .card {
    position: absolute;
    left: 49px;
    top: 49px;
    width: 1102px;
    height: 661px;
    background: linear-gradient(100deg, var(--gold-light) 0%, var(--gold-mid) 55%, var(--bronze-dark) 100%);
    color: var(--ink-light);
  }
  .firm-lockup {
    position: absolute;
    left: 88px;
    top: 240px;
    font-family: "EB Garamond", Georgia, serif;
    font-weight: 400;
    color: var(--ink-light);
    line-height: 1;
  }
  .firm-lockup .firm-prefix {
    display: block;
    font-size: 24px;
    letter-spacing: 3px;
    text-transform: uppercase;
    margin-bottom: 8px;
  }
  .firm-lockup .firm-first {
    display: block;
    font-size: 60px;
    margin-bottom: 2px;
  }
  .firm-lockup .firm-last {
    display: block;
    font-size: 60px;
  }
  .website {
    position: absolute;
    left: 378px;
    top: 380px;
    font-family: "Arimo", Arial, sans-serif;
    font-style: italic;
    font-size: 28px;
    color: var(--ink-light);
  }
  .practice-areas {
    position: absolute;
    left: 653px;
    top: 240px;
    list-style: none;
    font-family: "Arimo", Arial, sans-serif;
    font-size: 32px;
    line-height: 44px;
    color: var(--ink-light);
  }
</style>
</head>
<body>
  <div class="sheet">
    <div class="card">
      <div class="firm-lockup">
        <span class="firm-prefix">Law Offices of</span>
        <span class="firm-first">Tobin</span>
        <span class="firm-last">Haskell, PA</span>
      </div>
      <div class="website">haskelllaw.com</div>
      <ul class="practice-areas">
        <li>Civil Litigation</li>
        <li>Corporate Law</li>
        <li>Business Governance</li>
        <li>Real Estate Law</li>
      </ul>
    </div>

    <svg class="crop-marks" width="1200" height="759" viewBox="0 0 1200 759" aria-hidden="true">
      <g stroke="var(--crop-mark)" stroke-width="1.5">
        <!-- top left -->
        <line x1="84" y1="0" x2="84" y2="36"/>
        <line x1="0" y1="84" x2="36" y2="84"/>
        <!-- top right -->
        <line x1="1116" y1="0" x2="1116" y2="36"/>
        <line x1="1164" y1="84" x2="1200" y2="84"/>
        <!-- bottom left -->
        <line x1="84" y1="723" x2="84" y2="759"/>
        <line x1="0" y1="675" x2="36" y2="675"/>
        <!-- bottom right -->
        <line x1="1116" y1="723" x2="1116" y2="759"/>
        <line x1="1164" y1="675" x2="1200" y2="675"/>
      </g>
    </svg>
  </div>
</body>
</html>
```